Cooler Trailer Rental Flyer

I need a flyer designed to showcase a rental product.

We own two refrigerated Cooler Trailers. One trailer is 7’ x 12’. The second trailer is 7’ x 16’. Each unit is a double axle trailer with a cargo capacity of 8000 lbs. The refrigeration unit is 110v and is capable of cooling or freezing with just 12 amps. The 12’ unit comes with a securely mounted generator for stand-alone service needs, and we have a portable generator available if needed for the 16’ unit.

The trailer requires a class III or class IV hitch, with a 2 5/16” ball for towing and a 7-pin two vehicle socket for the trailer wiring.

We offer delivery for $1.40 per loaded mile (we only charge for the miles with the trailer attached, so one way for delivery or pickup). This option may make sense for many reasons, including:
- saving the cost of your time
- saving the cost of fuel
- eliminating your liability for the trailer while towing
- preventing you from having to buy any towing equipment

Our farm is located at 4127 Halvern Mills Avenue, Halvern Mills, Michigan 48672. The name of the farm/business is Maple Hollow Farm.

The rental rates are as follows:
$169/day (two day minimum rental required)
$599/week
$1500/month

A $100 deposit is required to reserve the trailer. The deposit is fully refundable up to two weeks prior to the event, 50% up to one week, and non-refundable within one week of the event.

The website for the place we bought the trailer is www.frostvanhaul.example. A link to a video from his website is https://frostvanhaul.example/refrigerated-trailer-videos/

I would like the flyer to be colorful and professional, with photos.
Updates

Several notes: 1. I have added the logo for Maple Hollow Farm. 2. Contact information for the brochure should be as follows: Martin or Colleen Verlander Maple Hollow Farm 5816 Maple Hollow Drive SW Halvern Mills, MI 48672 (616) 555-0147 3. Please note that we are not "FrostVanHaul.example". This is the website for the manufacturer of the trailers.

Here are some rental ideas that might be worth including: Emergencies and Power Outages Food Distributors Food Vendors Restaurants Caterers Ice Vendors Pubs and Microbreweries Resorts Festivals Open Markets Sporting Events Parties Weddings Floral Distributors Meat Processors Hunters

e-mail address is maplehollowfarm@mailbox.example

Target Market(s)

Food distributors, caterers, resorts, events (festivals, weddings, fairs, parades, parties, concerts), restaurants, breweries, farmers markets, vending companies, big game hunters

Font styles to use
Serif
Sans Serif

Colors

Designer to choose colors to be used in the design.

Requirements
Nice to have
• Tri-fold flyer

```html
<!DOCTYPE html>
<html lang="en">
<head>
<meta charset="utf-8">
<title>Maple Hollow Farm – Cooler Trailer Rental Tri-fold</title>
<link rel="stylesheet" href="https://fonts.googleapis.com/css2?family=Lato:ital,wght@0,400;0,700;0,900;1,400;1,700&display=swap">
<style>
  :root {
    --navy: #1d2a85;
    --navy-deep: #17216c;
    --yellow: #f3e61b;
    --paper: #ffffff;
    --paper-soft: #f3f4f7;
    --ink: #1f2340;
    --stage: #d9d9d9;
    --photo-sky: #c9d6e6;
    --photo-ground: #a89f8c;
  }
  * { box-sizing: border-box; margin: 0; padding: 0; }
  html, body { width: 1200px; height: 2400px; overflow: hidden; }
  body {
    background: var(--stage);
    font-family: "Lato", Arial, sans-serif;
    color: var(--ink);
  }
  .spread {
    position: absolute;
    left: 50px;
    width: 1100px;
    height: 850px;
    display: flex;
    background: var(--paper);
    box-shadow: 0 10px 30px rgba(0,0,0,.18);
  }
  .spread--outside { top: 250px; }
  .spread--inside { top: 1300px; }
  .panel {
    width: 366.67px;
    height: 100%;
    position: relative;
    display: flex;
    flex-direction: column;
    overflow: hidden;
  }
  .panel + .panel { border-left: 1px solid rgba(0,0,0,.06); }
  .photo {
    background: linear-gradient(180deg, var(--photo-sky) 0%, #e8edf2 45%, #d6d2c8 60%, var(--photo-ground) 100%);
  }
  .panel--navy { background: var(--navy); color: #fff; }

  /* Outside: back flap */
  .back-flap .photo { height: 530px; }
  .farm-note {
    flex: 1;
    padding: 40px 34px;
    font-style: italic;
    font-weight: 700;
    font-size: 19px;
    line-height: 1.45;
    color: var(--navy);
  }

  /* Outside: contact panel */
  .contact-panel .contact-block {
    flex: 1;
    background: var(--navy);
    color: #fff;
    padding: 110px 30px 0;
    text-align: center;
    font-size: 17px;
    line-height: 1.5;
  }
  .contact-item { margin-bottom: 38px; }
  .contact-item svg { display: block; margin: 0 auto 8px; }
  .social-strip {
    height: 190px;
    background: var(--paper);
    display: flex;
    justify-content: center;
    align-items: center;
    gap: 22px;
  }
  .social-dot {
    width: 38px; height: 38px;
    border: 2px solid var(--navy);
    border-radius: 50%;
  }

  /* Outside: cover */
  .cover .farm-name {
    height: 190px;
    display: flex;
    align-items: center;
    justify-content: center;
    gap: 14px;
    font-weight: 900;
    font-size: 34px;
    color: var(--ink);
  }
  .farm-name .mark {
    width: 22px; height: 22px; border-radius: 50%; background: var(--ink);
  }
  .cover .photo { height: 360px; }
  .cover-title {
    flex: 1;
    background: var(--navy);
    color: #fff;
    font-weight: 900;
    font-size: 44px;
    line-height: 1.15;
    text-align: center;
    display: flex;
    align-items: center;
    justify-content: center;
    padding: 0 30px;
  }

  /* Inside: about */
  .about { background: var(--paper-soft); }
  .about-copy { padding: 34px 30px 20px; }
  .section-label {
    font-weight: 900;
    font-size: 20px;
    color: var(--navy);
    display: inline-block;
    border-bottom: 3px solid var(--navy);
    margin-bottom: 16px;
  }
  .about-copy p {
    font-size: 15.5px;
    line-height: 1.5;
    text-align: justify;
  }
  .about .photo { height: 240px; margin-top: 12px; }
  .hitch-note {
    padding: 30px 30px;
    font-weight: 900;
    font-size: 19px;
    line-height: 1.4;
    color: var(--navy);
  }

  /* Inside: rates */
  .rates { padding: 34px 30px; font-size: 16px; line-height: 1.4; }
  .highlight { color: var(--yellow); font-weight: 900; }
  .rates .lead { font-size: 18px; margin-bottom: 22px; }
  .rates .sub { margin-bottom: 10px; font-size: 16px; }
  .tick-list { list-style: none; margin-bottom: 26px; }
  .tick-list li {
    display: flex; gap: 10px; align-items: flex-start;
    margin-bottom: 8px;
  }
  .tick-list svg { flex: none; margin-top: 3px; }
  .rates-heading { font-size: 22px; margin-bottom: 12px; }
  .rate-list li { font-size: 19px; }
  .rate-list .note { font-size: 12px; font-weight: 400; color: #fff; }
  .deposit-band {
    background: var(--yellow);
    color: var(--navy);
    font-weight: 900;
    font-size: 15px;
    text-align: center;
    padding: 8px 6px;
    margin: 0 -30px 20px;
  }

  /* Inside: gallery */
  .gallery { background: var(--paper-soft); padding: 28px 30px; gap: 18px; }
  .gallery-title {
    background: var(--navy);
    color: #fff;
    font-weight: 900;
    font-size: 20px;
    text-align: center;
    padding: 10px 0;
  }
  .gallery .photo {
    flex: 1;
    border: 4px solid var(--navy);
  }
  .gallery .photo--interior {
    background: linear-gradient(180deg, #eef0f2, #c7cbd1);
  }
</style>
</head>
<body>

<section class="spread spread--outside" aria-label="Brochure outside">
  <div class="panel back-flap">
    <div class="photo" role="img" aria-label="Photo of three white refrigerated cooler trailers parked on gravel under a cloudy sky"></div>
    <p class="farm-note">Our farm offers fresh produce and flowers, as well as hanging plants and pumpkins! During the season, please stop by our roadside stand at 4127 Halvern Mills Avenue!</p>
  </div>

  <div class="panel contact-panel">
    <div class="contact-block">
      <div class="contact-item">
        <svg width="22" height="22" viewBox="0 0 24 24" fill="none" stroke="#fff" stroke-width="2"><path d="M12 22s7-7 7-12a7 7 0 0 0-14 0c0 5 7 12 7 12z"/><circle cx="12" cy="10" r="2.5"/></svg>
        4127 Halvern Mills Avenue<br>Halvern Mills, MI 48672
      </div>
      <div class="contact-item">
        <svg width="22" height="22" viewBox="0 0 24 24" fill="none" stroke="#fff" stroke-width="2"><path d="M5 3h4l2 5-3 2a12 12 0 0 0 6 6l2-3 5 2v4a2 2 0 0 1-2 2A18 18 0 0 1 3 5a2 2 0 0 1 2-2z"/></svg>
        (616) 555-0147
      </div>
      <div class="contact-item">
        <svg width="24" height="20" viewBox="0 0 24 20" fill="none" stroke="#fff" stroke-width="2"><rect x="2" y="3" width="20" height="14"/><path d="M2 3l10 8 10-8"/></svg>
        maplehollowfarm@mailbox.example
      </div>
      <div class="contact-item">
        <svg width="22" height="22" viewBox="0 0 24 24" fill="none" stroke="#fff" stroke-width="2"><circle cx="12" cy="12" r="9"/><path d="M3 12h18M12 3c3 3 3 15 0 18M12 3c-3 3-3 15 0 18"/></svg>
        www.maplehollowfarm.example
      </div>
    </div>
    <div class="social-strip" aria-label="Social media">
      <span class="social-dot"></span><span class="social-dot"></span><span class="social-dot"></span><span class="social-dot"></span>
    </div>
  </div>

  <div class="panel cover">
    <div class="farm-name"><span class="mark"></span>Maple Hollow Farm</div>
    <div class="photo" role="img" aria-label="Photo of a white refrigerated cooler trailer with roof-mounted cooling unit parked on gravel"></div>
    <h1 class="cover-title">Cooler Trailer Rental</h1>
  </div>
</section>

<section class="spread spread--inside" aria-label="Brochure inside">
  <div class="panel about">
    <div class="about-copy">
      <h2 class="section-label">About</h2>
      <p>We have two refrigerated Cooler Trailer models available. One trailer is 7’ x 12’. The second trailer is 7’ x 16’. Each unit is a double axle trailer with a cargo capacity of 8000 lbs. The refrigeration unit is 110v and is capable of cooling or freezing with just 12 amps. The 12’ unit comes with a securely mounted generator for stand-alone service needs, and we have a portable generator available if needed for the 16’ unit.</p>
    </div>
    <div class="photo" role="img" aria-label="Photo of a white cooler trailer hitched to a pickup truck"></div>
    <p class="hitch-note">The trailer requires a class III or class IV hitch, with a 2 5/16” ball for towing and a 7-pin two vehicle socket for the trailer wiring.</p>
  </div>

  <div class="panel panel--navy rates">
    <p class="lead highlight">We offer delivery for $1.40 per loaded mile.</p>
    <p class="sub highlight">This option may make sense for many reasons, including:</p>
    <ul class="tick-list">
      <li><svg width="14" height="12" viewBox="0 0 14 12"><path d="M1 6l4 4 8-9" fill="none" stroke="#f3e61b" stroke-width="2.4"/></svg>Saving the cost of your time</li>
      <li><svg width="14" height="12" viewBox="0 0 14 12"><path d="M1 6l4 4 8-9" fill="none" stroke="#f3e61b" stroke-width="2.4"/></svg>Saving the cost of fuel</li>
      <li><svg width="14" height="12" viewBox="0 0 14 12"><path d="M1 6l4 4 8-9" fill="none" stroke="#f3e61b" stroke-width="2.4"/></svg>Eliminating your liability for the trailer while towing</li>
      <li><svg width="14" height="12" viewBox="0 0 14 12"><path d="M1 6l4 4 8-9" fill="none" stroke="#f3e61b" stroke-width="2.4"/></svg>Preventing you from having to buy any towing equipment</li>
    </ul>
    <p class="rates-heading highlight">The rental rates are as follows:</p>
    <ul class="tick-list rate-list">
      <li class="highlight"><svg width="14" height="12" viewBox="0 0 14 12"><path d="M1 6l4 4 8-9" fill="none" stroke="#f3e61b" stroke-width="2.4"/></svg><span>$169/day <span class="note">(two day minimum rental required)</span></span></li>
      <li class="highlight"><svg width="14" height="12" viewBox="0 0 14 12"><path d="M1 6l4 4 8-9" fill="none" stroke="#f3e61b" stroke-width="2.4"/></svg>$599/week</li>
      <li class="highlight"><svg width="14" height="12" viewBox="0 0 14 12"><path d="M1 6l4 4 8-9" fill="none" stroke="#f3e61b" stroke-width="2.4"/></svg>$1500/month</li>
    </ul>
    <p class="deposit-band">A $100 deposit is required to reserve the trailer.</p>
    <ul class="tick-list">
      <li><svg width="14" height="12" viewBox="0 0 14 12"><path d="M1 6l4 4 8-9" fill="none" stroke="#f3e61b" stroke-width="2.4"/></svg>The deposit is 100% refundable up to two weeks prior to the rental period.</li>
      <li><svg width="14" height="12" viewBox="0 0 14 12"><path d="M1 6l4 4 8-9" fill="none" stroke="#f3e61b" stroke-width="2.4"/></svg>The deposit is 50% refundable up to one week prior to the rental period.</li>
      <li><svg width="14" height="12" viewBox="0 0 14 12"><path d="M1 6l4 4 8-9" fill="none" stroke="#f3e61b" stroke-width="2.4"/></svg>The deposit is non-refundable within one week of the rental period.</li>
    </ul>
  </div>

  <div class="panel gallery">
    <h2 class="gallery-title">Cooler Trailer Rental</h2>
    <div class="photo" role="img" aria-label="Photo of two cooler trailers side by side"></div>
    <div class="photo" role="img" aria-label="Photo of a cooler trailer with rear doors open"></div>
    <div class="photo" role="img" aria-label="Photo of a white cooler trailer from the side"></div>
    <div class="photo photo--interior" role="img" aria-label="Photo of the empty insulated trailer interior"></div>
  </div>
</section>

</body>
</html>
```